Gestatlung flyer (2 pages) format selectable, based accompanying templates (logo, text) Projektflyer "intercultural cooking class with asylum seekers' data Friday evenings 17. 03 / 24.03 / 31.03 / 07.04 / Time: 18:30 Location: KL Marbeck St. Gallen Title: Intercultural cooking class with asylum seekers text: cooking course is run by asylum seekers. Cooking together, outlandish specialties, exciting conversations Registration: until 24h before the event costs: Expenses participation at its discretion Logos: Pepper Grove, Stifung Valmora. The logos should be listed as the sender and do not dominate the flyer. --------- Just be creative, everything is permitted and desired. The goal is that we make as many people as possible aware of this flyer. The flyers are distributed and the target audience is young adults. Dr Flyer should be correspondingly Modern, Emotianal and sales driven (screaming). Strong Typo, clearly legible and the content clearly structured. The shape of the flyer is free! In total we leave you as much creative freedom as possible. I am looking forward to the many great suggestions and am very excited about the results.

Target Market(s)

Young adults

Font styles to use
Serif
Sans Serif
Script

Requirements
Must have
• Textunterstüzung by appropriate images. Friendly design, bright colors. Very easy to read, weighted Title entsrprechend.
Nice to have
• Emotional Cook image or illustration
Should not have
• No picture with white and dark-skinned people.

```html
<!DOCTYPE html>
<html lang="de">
<head>
<meta charset="utf-8">
<title>Interkultureller Kochkurs – Flyer</title>
<link rel="stylesheet" href="https://fonts.googleapis.com/css2?family=Roboto+Condensed:wght@700&family=Bitter:wght@400;800&family=Lato:wght@400;700&display=swap">
<style>
  :root{
    --magenta:#f23ae6;
    --cyan:#3ef0f0;
    --lime:#9df02c;
    --ink:#2b2b2b;
    --panel:#383838;
    --white:#ffffff;
    --page:#ffffff;
    --photo-warm:#b87a5c;
    --photo-mid:#d9a07a;
    --photo-cool:#8a6a58;
  }
  html,body{margin:0;padding:0;width:1200px;height:1200px;overflow:hidden;background:var(--page);}
  .flyer{position:absolute;left:224px;top:73px;width:752px;height:1054px;overflow:hidden;
    box-shadow:0 4px 14px rgba(0,0,0,.35);font-family:"Lato",sans-serif;color:var(--ink);}
  .flyer-art{position:absolute;inset:0;}
  .abs{position:absolute;margin:0;}
  .title{left:30px;top:532px;font-family:"Roboto Condensed",sans-serif;font-weight:700;font-size:60px;line-height:60px;letter-spacing:-0.5px;}
  .title .t-pink{color:var(--magenta);display:block;}
  .title .t-cyan{color:var(--cyan);display:block;}
  .title .t-serif{display:block;font-family:"Bitter",serif;font-weight:400;font-size:52px;color:var(--ink);letter-spacing:0;}
  .features{list-style:none;padding:0;font-size:12px;line-height:14px;color:#444;}
  .features li{position:relative;padding-left:9px;margin-bottom:12px;}
  .features li::before{content:"";position:absolute;left:0;top:5px;width:4px;height:4px;border-radius:50%;background:var(--magenta);}
  .features-a{left:30px;top:748px;width:160px;}
  .features-b{left:235px;top:748px;width:160px;}
  .cost{left:31px;top:844px;font-size:20px;line-height:26px;font-weight:700;color:#333;width:380px;}
  .call{left:28px;top:918px;font-family:"Roboto Condensed",sans-serif;font-weight:700;font-size:34px;color:var(--ink);}
  .call .call-label{color:var(--magenta);margin-right:12px;}
  .web{left:31px;top:974px;font-size:15px;color:#444;}
  .info-label{font-family:"Roboto Condensed",sans-serif;font-weight:700;font-size:38px;color:var(--magenta);line-height:40px;}
  .info-rule{position:absolute;height:4px;background:var(--cyan);}
  .days{left:464px;top:650px;font-family:"Bitter",serif;font-weight:800;font-variant:small-caps;font-size:19px;color:var(--cyan);letter-spacing:.5px;}
  .dates{left:464px;top:678px;font-size:17px;color:var(--white);}
  .time{left:469px;top:762px;font-size:36px;color:var(--white);}
  .place{left:474px;top:878px;font-size:20px;color:var(--white);}
  .sender{left:478px;top:972px;display:flex;align-items:center;gap:12px;font-size:34px;font-weight:400;color:var(--white);}
  .sender-dot{width:14px;height:14px;border-radius:50%;background:var(--magenta);}
</style>
</head>
<body>
<article class="flyer">
  <svg class="flyer-art" width="752" height="1054" viewBox="0 0 752 1054" aria-hidden="false">
    <defs>
      <linearGradient id="photoTone" x1="0" y1="0" x2="1" y2="1">
        <stop offset="0" stop-color="var(--photo-warm)"/>
        <stop offset=".5" stop-color="var(--photo-mid)"/>
        <stop offset="1" stop-color="var(--photo-cool)"/>
      </linearGradient>
      <linearGradient id="circleTone" x1="0" y1="0" x2="1" y2="1">
        <stop offset="0" stop-color="#e6d2bc"/>
        <stop offset="1" stop-color="#a88466"/>
      </linearGradient>
    </defs>
    <g role="img" aria-label="Foto: eine Gruppe junger Leute kocht gemeinsam mit einem Koch in einer Küche mit frischem Gemüse">
      <rect x="0" y="0" width="752" height="540" fill="url(#photoTone)"/>
    </g>
    <path class="page-white" d="M0 505 C200 550 420 500 560 480 L752 500 L752 1054 L0 1054Z" fill="var(--white)"/>
    <path class="info-panel" d="M446 1054 L446 505 C560 478 680 484 752 512 L752 1054Z" fill="var(--panel)"/>
    <path class="wave-magenta" d="M0 420 C200 470 420 430 560 405 C650 392 720 418 752 440 L752 466 C700 446 640 428 560 440 C420 462 200 500 0 458Z" fill="var(--magenta)"/>
    <path class="wave-cyan" d="M0 468 C200 508 420 470 560 452 C660 440 720 466 752 482 L752 510 C700 490 640 472 560 478 C420 492 200 522 0 492Z" fill="var(--cyan)"/>
    <path class="wave-lime" d="M0 496 C200 528 420 496 560 482 L560 492 C420 508 200 540 0 512Z" fill="var(--lime)"/>
    <circle cx="542" cy="472" r="114" fill="var(--lime)"/>
    <circle cx="542" cy="472" r="107" fill="var(--magenta)"/>
    <circle cx="542" cy="472" r="102" fill="var(--white)"/>
    <circle cx="542" cy="472" r="98" fill="var(--cyan)"/>
    <g role="img" aria-label="Rundes Foto: Koch und zwei Teilnehmerinnen bereiten Essen zu">
      <circle cx="542" cy="472" r="93" fill="url(#circleTone)"/>
    </g>
    <rect class="bottom-bar" x="0" y="1020" width="446" height="34" fill="var(--magenta)"/>
  </svg>

  <h1 class="abs title">
    <span class="t-pink">Interkultureller</span>
    <span class="t-cyan">Kochkurs mit</span>
    <span class="t-serif">Asylsuchenden</span>
  </h1>

  <ul class="abs features features-a">
    <li>Kochkurs wird von Asylsuchenden geleitet</li>
    <li>Gemeinsames Kochen</li>
  </ul>
  <ul class="abs features features-b">
    <li>Fremdländische</li>
    <li>Spezialiäten</li>
    <li>Spannende Gespräche</li>
  </ul>

  <p class="abs cost">Unkostenbeteiligung nach eigenem Ermessen</p>
  <p class="abs call"><span class="call-label">CALL NOW</span>0123456789</p>
  <p class="abs web">www.companywebsite.com</p>

  <h2 class="abs info-label" style="left:462px;top:604px;">Daten</h2>
  <span class="info-rule" style="left:556px;top:629px;width:164px;"></span>
  <p class="abs days">Freitag Abende</p>
  <p class="abs dates">17.03 / 24.03 / 31.03 / 07.04/</p>

  <h2 class="abs info-label" style="left:466px;top:720px;">Zeit:</h2>
  <span class="info-rule" style="left:546px;top:745px;width:170px;"></span>
  <p class="abs time">18.30h</p>

  <h2 class="abs info-label" style="left:464px;top:826px;">Ort:</h2>
  <span class="info-rule" style="left:542px;top:846px;width:170px;"></span>
  <p class="abs place">KL Marbeck St.Gallen</p>

  <p class="abs sender"><span class="sender-dot"></span>Pepper Grove</p>
</article>
</body>
</html>
```